依頼詳細
水色を基点とし2〜3色の構成で作成していただきたいです。
まるで水族館のようなテーマで考えております。
記載項目
パルモアフェスタリボン 日曜だけ! ちょぴっとお得♪
サイズ
• 320×100
希望イメージ
シンプル 複雑
単色 カラフル
暗い 明るい
日常 高級
遊び心 厳粛
未来的 伝統的
女性的 男性的
希望する色
水色系
納品ファイル
• 高解像度JPG (.jpg)
補足説明
依頼方法をミスしてしまったのですが追記で修正したものを載せさせていただきます。
こちらのファイルのようなものをお願いできますか?
フェスタリボンなので夜っぽくても明るめな仕上がりでお願いしたいです。

デザインが良かった

作成していただきありがとうございました。

```html
<!DOCTYPE html>
<html lang="ja">
<head>
<meta charset="utf-8">
<title>パルモアフェスタリボン バナー</title>
<link rel="stylesheet" href="https://fonts.googleapis.com/css2?family=Shippori+Mincho:wght@600&family=M+PLUS+Rounded+1c:wght@700&display=swap">
<style>
  :root {
    --sky-deep: #1f6fd8;
    --sky-mid: #3fa0ee;
    --sky-light: #8fdcf6;
    --sky-glow: #c8f1fb;
    --moon-pale: rgba(251, 246, 210, 0.55);
    --figure-violet: rgba(165, 139, 224, 0.55);
    --figure-blue: rgba(124, 182, 240, 0.45);
    --text-white: #ffffff;
    --text-outline: #2a4fa8;
  }
  html, body {
    margin: 0;
    padding: 0;
    width: 1200px;
    height: 375px;
    overflow: hidden;
    background: #ffffff;
  }
  .banner {
    position: relative;
    width: 1200px;
    height: 375px;
    overflow: hidden;
    background:
      radial-gradient(ellipse 55% 45% at 35% 75%, var(--sky-glow) 0%, transparent 70%),
      radial-gradient(ellipse 60% 60% at 20% 40%, var(--sky-light) 0%, transparent 75%),
      linear-gradient(180deg, var(--sky-deep) 0%, var(--sky-mid) 45%, var(--sky-light) 100%);
  }
  .starry-sky {
    position: absolute;
    inset: 0;
    background:
      radial-gradient(ellipse 40% 30% at 70% 20%, rgba(255,255,255,0.25) 0%, transparent 70%),
      radial-gradient(ellipse 35% 25% at 10% 90%, rgba(255,255,255,0.3) 0%, transparent 70%);
  }
  .moon-and-figure {
    position: absolute;
    left: 600px;
    top: 0;
    width: 600px;
    height: 375px;
    background:
      radial-gradient(ellipse 22% 45% at 22% 45%, var(--moon-pale) 0%, transparent 100%),
      radial-gradient(ellipse 28% 50% at 58% 78%, var(--figure-violet) 0%, transparent 100%),
      radial-gradient(ellipse 30% 55% at 72% 85%, var(--figure-blue) 0%, transparent 100%);
  }
  .title {
    position: absolute;
    left: 128px;
    top: 124px;
    margin: 0;
    font-family: "Shippori Mincho", serif;
    font-weight: 600;
    font-size: 70px;
    line-height: 1;
    letter-spacing: 12px;
    color: var(--text-white);
    text-shadow: 0 0 3px rgba(30, 70, 160, 0.9), 0 0 10px rgba(40, 90, 190, 0.6);
    white-space: nowrap;
  }
  .tagline {
    position: absolute;
    left: 144px;
    top: 238px;
    margin: 0;
    font-family: "M PLUS Rounded 1c", sans-serif;
    font-weight: 700;
    font-size: 44px;
    line-height: 1;
    letter-spacing: 5px;
    color: var(--text-white);
    -webkit-text-stroke: 3px var(--text-outline);
    paint-order: stroke fill;
    white-space: nowrap;
  }
</style>
</head>
<body>
  <main class="banner">
    <div class="starry-sky" role="img" aria-label="きらめく星が散りばめられた水色の夜空"></div>
    <div class="moon-and-figure" role="img" aria-label="三日月と、それを見上げる人物のシルエットのイラスト"></div>

    <h1 class="title">パルモアフェスタリボン</h1>
    <p class="tagline">日曜だけ！ちょぴっとお得♪</p>
  </main>
</body>
</html>
```